Business Card Design

We need a business card design for a new company called Velmar Joinery. We make, design and install all joinery.
We want a classy business card which is not to busy, we want a double sided card with just the logo on one side and all the required information on the other. We are a partnership so would like cards with both names and numbers. We would like to see a design which blends in with our logo and really makes it pop.

Reason: I would like my logo displayed on the business card please.

Industry/Entity Type

Business

Contact Information for Business Card

Name- Dean Velmar Phone Number- 047318562
Name- Luke Velmar Phone Number- 0418265931 E-mail- velmarjoinery@examplemail.net
License Number- 583920k Company Name- Velmar Joinery ABN-47 508 293 614

Colors
0456a4
ffffff

```html
<!DOCTYPE html>
<html lang="en">
<head>
<meta charset="utf-8">
<title>Velmar Joinery – Business Cards</title>
<link href="https://fonts.googleapis.com/css2?family=Open+Sans:wght@400;600;700&display=swap" rel="stylesheet">
<style>
  :root {
    --brand-blue: #0456a4;
    --paper: #ffffff;
    --ink: #1c1c1c;
    --ink-soft: #3a3a3a;
    --backdrop: #6b6b6b;
    --block-black: #1a1a1a;
  }
  * { box-sizing: border-box; margin: 0; padding: 0; }
  html, body { width: 1200px; height: 1000px; overflow: hidden; }
  body {
    background: var(--backdrop);
    font-family: "Open Sans", Arial, sans-serif;
    color: var(--ink);
    position: relative;
  }
  .card {
    position: absolute;
    width: 560px;
    height: 320px;
    background: var(--paper);
    box-shadow: 0 14px 30px rgba(0,0,0,.35);
    overflow: hidden;
  }
  .card--front { left: 70px; top: 120px; }
  .card--back { left: 570px; top: 540px; }

  /* wordmark */
  .wordmark {
    position: absolute;
    display: flex;
    align-items: center;
    gap: 14px;
  }
  .wordmark__square {
    width: 46px; height: 46px;
    background: var(--brand-blue);
    border-radius: 6px;
  }
  .wordmark__name {
    font-weight: 700;
    font-size: 34px;
    letter-spacing: 1px;
    color: var(--brand-blue);
    text-transform: uppercase;
  }
  .card--front .wordmark { left: 50px; top: 96px; }
  .card--back .wordmark { left: 210px; top: 34px; }
  .card--back .wordmark__square { width: 38px; height: 38px; }
  .card--back .wordmark__name { font-size: 28px; }

  /* front band */
  .front-band {
    position: absolute;
    left: 34px; right: 0; top: 228px;
    height: 38px;
    background: var(--brand-blue);
    display: flex;
    align-items: center;
    justify-content: center;
    padding-left: 60px;
  }
  .front-band__stub {
    position: absolute;
    left: 0; top: 228px;
    width: 22px; height: 38px;
    background: var(--block-black);
  }
  .website {
    color: var(--paper);
    font-size: 17px;
    letter-spacing: 2px;
  }

  /* back band */
  .back-band {
    position: absolute;
    left: 110px; right: 0; top: 110px;
    height: 96px;
    background: var(--brand-blue);
    display: flex;
    align-items: center;
    justify-content: space-around;
    color: var(--paper);
  }
  .back-band__stub {
    position: absolute;
    left: 110px; top: 98px;
    width: 90px; height: 12px;
    background: var(--block-black);
  }
  .partner { line-height: 1.25; }
  .partner__name { font-weight: 700; font-size: 19px; }
  .partner__phone { font-size: 18px; letter-spacing: 1px; }

  .company-details {
    position: absolute;
    left: 30px; top: 218px;
    font-size: 15px;
    line-height: 1.35;
    color: var(--ink-soft);
  }
  .company-details__name { font-weight: 700; color: var(--ink); }
  .company-details__label { color: var(--brand-blue); }
</style>
</head>
<body>

<section class="card card--front" aria-label="Business card front">
  <div class="wordmark">
    <span class="wordmark__square"></span>
    <span class="wordmark__name">Velmar Joinery</span>
  </div>
  <div class="front-band__stub"></div>
  <div class="front-band">
    <span class="website">www.velmarjoinery.example</span>
  </div>
</section>

<section class="card card--back" aria-label="Business card back">
  <div class="wordmark">
    <span class="wordmark__square"></span>
    <span class="wordmark__name">Velmar Joinery</span>
  </div>
  <div class="back-band__stub"></div>
  <div class="back-band">
    <div class="partner">
      <div class="partner__name">Dean Velmar</div>
      <div class="partner__phone">047318562</div>
    </div>
    <div class="partner">
      <div class="partner__name">Luke Velmar</div>
      <div class="partner__phone">0418265931</div>
    </div>
  </div>
  <div class="company-details">
    <div class="company-details__name">Velmar Joinery</div>
    <div>License Number- 583920k</div>
    <div>ABN-47 508 293 614</div>
    <div><span class="company-details__label">M+</span> velmarjoinery@examplemail.net</div>
  </div>
</section>

</body>
</html>
```